The Driftwood Caster----- Wade Pellman----- Kellow Creek Bronzeback ------www.thedriftwoodcaster.test-----

Hello Fishermen,
The Umpqua rivers peaceful beauty is like no other river, the private Hollis section offers trophy bass fishing along with 100 fish days. Spin cast or fly fish for bass. This 8 hour fishing trip takes you into a remote section of ranches and wilderness abundant with not only thousands of bass per mile...... but wildlife and scenery are breath taking in this quite section of river.
This trip is for everyone, easy for the Grand Parents and the grand kids...... Women love this trip with the warm weather and easy fishing.
So Let's go Fishing...... please call or email us today and book your trip or with any questions you have.
Vacation Rentals, Motels and R.V parks all available close by.

Email us at: driftwoodcaster@mailbrook.test
Visit our website at: www.thedriftwoodcaster.test
Call us at: 541-555-0148

Thank you for fishing with us,
Wade Pellman

return address;
Wade Pellman
p.o. box 712
Elkton, Oregon 97521

****NOTE for front of post card layout person should go to our website home page for ideas, and photos. Please feel free to change our message above to correct grammar and make read smoother, Thank you.....

there is no contest....not sure how that got there...

```html
<!DOCTYPE html>
<html lang="en">
<head>
<meta charset="utf-8">
<title>The Driftwood Caster – Postcard</title>
<link href="https://fonts.googleapis.com/css2?family=Montserrat:wght@300;400;800&family=Oswald:wght@500&family=Open+Sans:ital,wght@0,700;1,400;1,700&display=swap" rel="stylesheet">
<style>
:root{
  --bg:#4a4647;
  --white:#ffffff;
  --teal:#0f7a8a;
  --teal-band:#137f90;
  --orange:#f37a1f;
  --yellow:#ffe21a;
  --ink:#2b2b2b;
  --strip:#1b1b1b;
  --navy:#25358c;
  --red:#d42027;
  --photo-water:#6f9aa8;
  --photo-green:#5f7a4c;
}
*{box-sizing:border-box;margin:0;padding:0}
html,body{width:793px;height:1200px;overflow:hidden;background:var(--bg)}
.canvas{position:relative;width:793px;height:1200px}
.card{position:absolute;left:63px;width:667px;background:var(--white);overflow:hidden}
.card--front{top:65px;height:513px}
.card--back{top:621px;height:514px}

/* front */
.brand{position:absolute;left:0;width:470px;top:26px;text-align:center;color:var(--teal);
  font:800 28px/1 "Montserrat",sans-serif;letter-spacing:.3px;white-space:nowrap}
.guide-name{position:absolute;left:0;width:470px;top:62px;text-align:center;color:var(--ink);
  font:300 28px/1 "Montserrat",sans-serif;letter-spacing:1.5px}
.hero-band{position:absolute;left:0;top:113px;width:520px;height:249px;background:var(--teal-band)}
.hero-photo{position:absolute;left:168px;top:113px;width:352px;height:249px;
  background:linear-gradient(180deg,#8fb4c6 0%,#5c8c6b 40%,#d8b22a 60%,#9aa4a6 100%)}
.ribbon{position:absolute;left:68px;top:98px;width:356px;height:27px}
.ribbon span{position:absolute;inset:0;display:flex;align-items:center;justify-content:center;
  color:var(--white);font:800 16px/1 "Montserrat",sans-serif;letter-spacing:.4px}
.headline{position:absolute;left:24px;top:146px;color:var(--white);
  font:500 31px/38px "Oswald",sans-serif;text-transform:uppercase}
.headline em{font-style:normal;color:var(--yellow)}
.features{position:absolute;left:0;top:362px;width:520px;height:28px;background:var(--strip);
  display:flex;align-items:center;gap:10px;padding-left:12px;
  color:var(--white);font:500 15px/1 "Oswald",sans-serif;text-transform:uppercase}
.features li{list-style:none;display:flex;align-items:center;gap:6px}
.features li::before{content:"";border-left:7px solid var(--yellow);border-top:6px solid transparent;border-bottom:6px solid transparent}
.contact{position:absolute;left:0;width:404px;text-align:center;color:var(--ink);font-family:"Montserrat",sans-serif;white-space:nowrap}
.contact--email{top:404px;font-size:14px;font-weight:400}
.contact--web{top:426px;font-size:14px;font-weight:400}
.contact--call{top:451px;font-size:19px;font-weight:800;color:var(--teal)}
.contact--address{top:482px;font-size:12.5px;font-weight:400}
.stay-badge{position:absolute;left:409px;top:389px;width:118px;height:118px;border-radius:50%;
  background:var(--orange);display:flex;align-items:center;justify-content:center;text-align:center}
.stay-badge p{transform:rotate(22deg);color:var(--white);font:700 12.5px/14px "Open Sans",sans-serif}
.polaroid{position:absolute;background:var(--white);padding:8px;box-shadow:0 1px 4px rgba(0,0,0,.35)}
.polaroid div{width:100%;height:100%}
.polaroid--one{left:476px;top:-2px;width:184px;height:150px;transform:rotate(5deg)}
.polaroid--two{left:500px;top:148px;width:176px;height:180px;transform:rotate(-4deg)}
.polaroid--three{left:500px;top:330px;width:176px;height:172px;transform:rotate(4deg)}

/* back */
.stamp-box{position:absolute;left:563px;top:26px;width:80px;height:93px;border:1px solid #555}
.message{position:absolute;left:23px;top:26px;color:var(--navy);font:italic 400 11.4px/15px "Open Sans",sans-serif}
.message b{font-weight:700}
.greeting{color:var(--red);font-weight:700;font-size:14px;margin-bottom:10px}
.message .p1{width:445px;margin-bottom:15px}
.message .p2{width:255px;margin-bottom:15px}
.message .p3{width:265px;font-weight:700}
.back-contacts{position:absolute;left:23px;top:293px;color:var(--navy);font:italic 700 14.5px/19.5px "Open Sans",sans-serif}
.back-contacts span{color:var(--red)}
.signoff{position:absolute;left:24px;top:366px;color:var(--navy);font:italic 700 14.5px/19.5px "Open Sans",sans-serif}
.signoff span{color:var(--red)}
.address-line{position:absolute;left:414px;width:201px;height:1px;background:#777}
</style>
</head>
<body>
<main class="canvas">

  <section class="card card--front" aria-label="Postcard front">
    <div class="hero-band"></div>
    <div class="hero-photo" role="img" aria-label="Guide in yellow rain gear holding a large fish on a forested river"></div>
    <h1 class="brand">THE DRIFTWOOD CASTER</h1>
    <p class="guide-name">WADE PELLMAN</p>
    <div class="ribbon">
      <svg width="356" height="27" viewBox="0 0 356 27"><polygon points="0,0 356,0 346,13.5 356,27 0,27 10,13.5" fill="#f37a1f"/></svg>
      <span>FISHING GUIDE AND OUTFITER</span>
    </div>
    <h2 class="headline">We offers<br>trophy bass<br><em>fishing trip</em><br>on Umpqua<br>River Hollis</h2>
    <ul class="features">
      <li>100 Fish Days</li>
      <li>Spin Cast or Fly Fish for Bass</li>
      <li>8 Hour Fishing Trip</li>
    </ul>
    <p class="contact contact--email">Email us at: driftwoodcaster@mailbrook.test</p>
    <p class="contact contact--web">Visit our website at: www.thedriftwoodcaster.test</p>
    <p class="contact contact--call">CALL US AT: 541-555-0148</p>
    <p class="contact contact--address">Address : PO Box 712 - Elkton, Oregon 97521</p>
    <div class="polaroid polaroid--one"><div role="img" aria-label="Three anglers in a boat showing their catch" style="background:linear-gradient(180deg,var(--photo-green),#8aa58c 55%,#d9d9d9)"></div></div>
    <div class="polaroid polaroid--two"><div role="img" aria-label="Smiling angler holding two fish in a boat" style="background:linear-gradient(180deg,#8aa0a8,#c7b48a 55%,#6d7d86)"></div></div>
    <div class="polaroid polaroid--three"><div role="img" aria-label="Guide boat moored on the river" style="background:linear-gradient(180deg,#5d6a70,#b9c3c6 45%,var(--photo-water))"></div></div>
    <div class="stay-badge"><p>Vacation<br>Rentals, Motels<br>and R.V parks<br>all available<br>close by.</p></div>
  </section>

  <section class="card card--back" aria-label="Postcard back">
    <div class="stamp-box"></div>
    <div class="message">
      <p class="greeting">Hello Fishermen,</p>
      <p class="p1">The Umpqua rivers peaceful beauty is like no other river, <b>the private Hollis section offers trophy bass fishing along with 100 fish days</b>. Spin cast or fly fish for bass. This 8 hour fishing trip takes you into a remote section of ranches and wilderness abundant with not only thousands of bass per mile...... but wildlife and scenery are breath taking in this quite section of river.</p>
      <p class="p2">This trip is for everyone, easy for the Grand Parents and the grand kids...... Women love this trip with the warm weather and easy fishing.</p>
      <p class="p3">So Let’s go Fishing<br>please call or email us today and book your trip or with any questions you have.<br>Vacation Rentals, Motels and R.V parks all available close by.</p>
    </div>
    <p class="back-contacts">Email us at: <span>driftwoodcaster@mailbrook.test</span><br>Visit at: <span>www.thedriftwoodcaster.test</span><br>Call us at: <span>541-555-0148</span></p>
    <p class="signoff">Thank you for fishing with us,<br><span>Wade Pellman</span></p>
    <div class="address-line" style="top:241px"></div>
    <div class="address-line" style="top:291px"></div>
    <div class="address-line" style="top:341px"></div>
  </section>

</main>
</body>
</html>
```